Harborlight Equity Corporate Profile

Redesign Corporate Profile with special attention to Cover, Dividers, Introduction of professional images, icons, colors, formatting among others. To visually enhance the 24 pages to give it a financial look with a young and fresh angle.
The PPT is a corporate profile which is a presentation about the company, its key milestones along with specific key case studies.
Images related to Dubai city, millennial consumer, globalization, technology should be included.
Target Market(s)
Investors, Brand Owners, Shareholders, Employees
Industry/Entity Type
Investment Advisory
Requirements
Must have
- Maintain current content and section structure
- Enhance cover, dividers
- Add professional images
- Enhance graphs and charts
- Add info-graphics

```html
<!DOCTYPE html>
<html lang="en">
<head>
<meta charset="utf-8">
<title>Harborlight Equity – Corporate Profile</title>
<link rel="stylesheet" href="https://fonts.googleapis.com/css2?family=Arimo:ital,wght@0,400;0,700;1,400&display=swap">
<style>
:root{
  --red:#e3262b;
  --ink:#1b1b1b;
  --night:#141212;
  --grey:#8c8c8c;
  --grey-mid:#6f6f6f;
  --panel:#e6e6e6;
  --white:#ffffff;
  --text:#333333;
}
*{margin:0;padding:0;box-sizing:border-box}
html,body{width:960px;height:1200px;overflow:hidden;background:var(--white)}
body{position:relative;font-family:"Arimo",Arial,sans-serif;color:var(--text)}
.slide{position:absolute;width:470px;height:264px;overflow:hidden;box-shadow:0 1px 4px rgba(0,0,0,.35)}
.col-l{left:5px}.col-r{left:485px}
.row-1{top:18px}.row-2{top:318px}.row-3{top:618px}.row-4{top:918px}
.abs{position:absolute}
.photo{position:absolute;inset:0}
.photo-city{background:radial-gradient(ellipse at 30% 40%,#3d3332 0%,#231d1c 45%,#0e0c0c 100%)}
.photo-night{background:linear-gradient(160deg,#2b2524 0%,#171313 55%,#0b0a0a 100%)}
.photo-skyline{background:radial-gradient(ellipse at 60% 80%,#4a2a22 0%,#1f1a19 50%,#0d0b0b 100%)}
.light{background:var(--white)}
.dark{background:var(--night)}

.brand{position:absolute;display:flex;align-items:center;gap:4px;font-weight:700;white-space:nowrap;letter-spacing:.02em}
.brand i{display:block;width:7px;height:7px;background:var(--red)}
.brand.on-dark{color:var(--white)}
.brand.on-light{color:var(--ink)}

.cover-band{position:absolute;left:106px;width:94px;background:var(--red);opacity:.9}
.cover-title{left:234px;top:118px;color:var(--white);font-weight:700;font-size:17.6px}
.cover-sub{left:234px;top:142px;color:var(--white);font-size:11px}
.cover-date{left:234px;top:161px;background:var(--red);color:var(--white);font-size:6.5px;padding:1px 4px}

.agenda-side{position:absolute;left:236px;top:0;width:234px;height:264px;background:var(--grey-mid)}
.quote{left:27px;top:128px;width:146px;color:var(--white);font-style:italic;font-size:7.6px;line-height:10.6px}
.quote-author{left:27px;top:199px;color:var(--white);font-style:italic;font-size:7.8px}
.agenda-title{left:285px;top:52px;color:var(--white);font-size:21px;font-weight:400;letter-spacing:.02em}
.agenda-list{position:absolute;left:267px;top:100px;list-style:none;color:var(--white);font-size:7.8px}
.agenda-list li{display:flex;height:26px}
.agenda-list b{font-weight:400;width:21px}

.divider-vline{position:absolute;left:38px;width:1px;background:#8a8585}
.divider-hline{position:absolute;height:1px;background:#8a8585}
.divider-title{color:var(--white);font-weight:700;font-size:21px}
.divider-sub{color:var(--red);font-weight:700;font-size:11px;letter-spacing:.02em}

.tab{position:absolute;left:11px;top:0;width:39px;height:5px;background:var(--red)}
.slide-title{left:12px;top:13px;font-weight:700;font-size:13.6px}
.dark .slide-title{color:var(--white)}
.light .slide-title{color:var(--ink)}
.footer-line{position:absolute;left:58px;right:22px;top:251px;height:1px;background:#555}
.url{position:absolute;top:250px;font-size:5.6px}
.dark .url{color:var(--white);left:370px}
.light .url{color:var(--red);left:369px}
.page-no{position:absolute;left:452px;top:242px;font-size:5.6px;color:var(--grey)}
.dark .page-no{color:var(--white)}

.stat-num{position:absolute;width:30px;text-align:center;color:var(--red);font-weight:700;font-size:17px}
.stat-sep{position:absolute;width:1px;height:26px;background:#777}
.stat-text{position:absolute;color:var(--white);font-size:11px;line-height:14px}

.subhead{font-weight:700;font-size:8px;color:var(--ink)}
.map{left:14px;top:62px;width:190px;height:172px;border-radius:4px;
  background:radial-gradient(ellipse 38% 20% at 62% 22%,#e3262b 0%,#e3262b 55%,rgba(227,38,43,0) 100%),
             radial-gradient(ellipse 14% 8% at 54% 90%,#e3262b 0%,#e3262b 50%,rgba(227,38,43,0) 100%),
             linear-gradient(160deg,#b4b4b4 0%,#9a9a9a 60%,#8a8a8a 100%)}
.map-key{left:19px;top:222px;display:flex;align-items:center;gap:3px;font-size:3.8px;color:var(--ink);background:rgba(255,255,255,.85);padding:1px 2px}
.map-key i{width:6px;height:6px;border-radius:50%;background:var(--red);display:block}
.pillar{position:absolute;top:32px;height:58px;width:56px;display:flex;align-items:center;justify-content:center;text-align:center;font-weight:700;font-size:6.1px;line-height:7.6px;padding:2px}
.pillar.grey{background:var(--grey);color:var(--white)}
.pillar.red{background:var(--red);color:var(--white)}
.pillar.black{background:#0d0d0d;color:var(--white)}
.pillar.pale{background:#d9d9d9;color:var(--ink);font-weight:400}
.num-dot{position:absolute;width:11px;height:11px;border:1px solid var(--grey);border-radius:50%;background:var(--white);font-size:5px;line-height:9px;text-align:center;color:var(--ink)}
.about-col{position:absolute;top:122px;width:112px;font-size:5.5px;line-height:7px;color:var(--ink);box-shadow:0 0 3px rgba(0,0,0,.15);padding:3px 4px;height:118px}
.about-col h4{font-size:6.2px;font-weight:700}
.about-col em{display:block;font-size:5.8px;margin-bottom:6px}
.about-col p{margin-bottom:6px}

.issue{position:absolute;left:11px;width:248px;background:var(--panel);font-size:5.6px;line-height:7px;color:var(--ink);padding:3px 4px 3px 14px}
.issue .dot{position:absolute;left:1px;top:50%;margin-top:-6px;width:11px;height:11px;border-radius:50%;background:var(--red);color:var(--white);font-size:5px;line-height:11px;text-align:center;font-weight:700}
.phase-title{left:0;width:270px;top:132px;text-align:center;font-size:7.8px;font-weight:700;color:var(--ink)}
.stage{position:absolute;border-top:3px solid var(--grey);font-size:4.8px;line-height:6px;color:var(--ink);padding:2px 0 0 6px}
.stage b{display:block;font-size:5.2px}
.benefit{position:absolute;left:293px;width:164px;background:var(--white);box-shadow:0 0 4px rgba(0,0,0,.25);padding:4px 6px;font-size:5.4px;line-height:6.6px;color:var(--ink)}
.benefit h4{color:var(--red);font-size:6.4px;margin-bottom:4px}
.benefit ul{list-style:none}
.benefit li{position:relative;padding-left:9px;margin-bottom:.5px}
.benefit li::before{content:"✓";position:absolute;left:0;color:var(--red);font-weight:700}

.case-row{position:absolute;left:27px;width:420px}
.case-label{position:absolute;left:72px;top:0;width:56px;height:100%;display:flex;align-items:center;justify-content:center;text-align:center;color:var(--white);font-weight:700;font-size:6.4px;line-height:8px}
.case-text{position:absolute;left:136px;top:0;right:0;height:100%;background:var(--panel);border-top:1.5px solid var(--red);font-size:5.6px;line-height:7.1px;color:var(--ink);padding:4px 6px 0 14px}
.case-text b{font-weight:700}
.case-icon{position:absolute;left:0;top:0;width:52px;height:100%}
</style>
</head>
<body>

<section class="slide col-l row-1 dark">
  <div class="photo photo-skyline" role="img" aria-label="Night photograph of the Dubai skyline with a sail-shaped hotel tower"></div>
  <div class="cover-band" style="top:0;height:108px"></div>
  <div class="cover-band" style="top:156px;height:108px"></div>
  <div class="brand on-dark" style="left:96px;top:126px;font-size:10px"><i></i>Harborlight Equity</div>
  <h1 class="abs cover-title">HARBORLIGHT EQUITY</h1>
  <p class="abs cover-sub">Global Growth with Local Expertise</p>
  <span class="abs cover-date">October 2017</span>
</section>

<section class="slide col-r row-1 dark">
  <div class="photo photo-night" role="img" aria-label="Dim photograph of a city at night"></div>
  <div class="agenda-side"></div>
  <div class="brand on-dark" style="left:27px;top:100px;font-size:10.5px"><i></i>Harborlight Equity</div>
  <p class="abs quote">“Our investment approach focuses on partnering with brands which are in the roll- out phase that require capital and local expertise to successfully enter and grow in international markets”</p>
  <p class="abs quote-author">Mara Ellison Founder &amp; CEO</p>
  <h2 class="abs agenda-title">AGENDA</h2>
  <ol class="agenda-list">
    <li><b>1</b>About Harborlight Equity</li>
    <li><b>2</b>Our Investments</li>
    <li><b>3</b>Why Partnering With Us</li>
    <li><b>4</b>Millennial Consumer Opportunity</li>
  </ol>
</section>

<section class="slide col-l row-2 dark">
  <div class="photo photo-city" role="img" aria-label="Dark aerial photograph of city towers"></div>
  <div class="brand on-dark" style="left:300px;top:52px;font-size:10px"><i></i>Harborlight Equity</div>
  <div class="divider-vline" style="top:146px;height:56px"></div>
  <div class="divider-hline" style="left:38px;width:195px;top:184px"></div>
  <h2 class="abs divider-title" style="left:46px;top:158px">SECTION 1:</h2>
  <p class="abs divider-sub" style="left:50px;top:189px">ABOUT HARBORLIGHT EQUITY</p>
</section>

<section class="slide col-r row-2 dark">
  <div class="photo photo-night" role="img" aria-label="Faint photograph of a city skyline at dusk"></div>
  <div class="tab"></div>
  <h2 class="abs slide-title">HARBORLIGHT EQUITY &nbsp;AT A GLANCE</h2>

  <span class="stat-num" style="left:25px;top:62px">5</span><span class="stat-sep" style="left:57px;top:60px"></span>
  <p class="stat-text" style="left:66px;top:59px">Reputable Private Equity<br>Investors from GCC</p>
  <span class="stat-num" style="left:25px;top:120px">10</span><span class="stat-sep" style="left:57px;top:118px"></span>
  <p class="stat-text" style="left:66px;top:117px">Experienced Management<br>Professionals in Dubai</p>
  <span class="stat-num" style="left:25px;top:177px">2</span><span class="stat-sep" style="left:57px;top:175px"></span>
  <p class="stat-text" style="left:66px;top:174px">Completed Investments<br>Over Last 12 Months</p>

  <span class="stat-num" style="left:225px;top:62px;width:44px">10%</span><span class="stat-sep" style="left:268px;top:60px"></span>
  <p class="stat-text" style="left:277px;top:59px">Dividend Yield After 18<br>Months of Operations</p>
  <span class="stat-num" style="left:230px;top:120px">2x</span><span class="stat-sep" style="left:268px;top:118px"></span>
  <p class="stat-text" style="left:277px;top:117px">Unrealized Cash on Cash<br>Return Since Inception</p>
  <span class="stat-num" style="left:230px;top:177px">4</span><span class="stat-sep" style="left:268px;top:175px"></span>
  <p class="stat-text" style="left:278px;top:170px">Operating Markets - UAE,<br>Saudi Arabia, South Africa<br>and Qatar</p>

  <div class="brand on-dark" style="left:12px;top:243px;font-size:6px"><i></i>Harborlight Equity</div>
  <div class="footer-line" style="left:80px"></div>
  <span class="url">www.harborlight-equity.example</span>
  <span class="page-no">6</span>
</section>

<section class="slide col-l row-3 light">
  <div class="tab"></div>
  <h2 class="abs slide-title" style="top:12px">About Harborlight Equity</h2>
  <p class="abs subhead" style="left:24px;top:47px">Harborlight Equity Key Markets Coverage</p>
  <div class="abs map" role="img" aria-label="Map of Africa and the Middle East in grey, with the GCC countries and South Africa highlighted in red as target markets"></div>
  <div class="abs map-key"><i></i>Target Markets</div>

  <div class="pillar grey" style="left:211px">Targets fundamental shifts in consumer behavior</div>
  <div class="pillar red" style="left:270px">Provides growth capital to companies in the roll-out stage</div>
  <div class="pillar black" style="left:330px">Partners with strong brand management teams</div>
  <div class="pillar pale" style="left:389px;width:58px">Develops and executes regional and multi-channel expansion</div>
  <span class="num-dot" style="left:205px;top:26px">1</span>
  <span class="num-dot" style="left:265px;top:26px">2</span>
  <span class="num-dot" style="left:325px;top:26px">3</span>
  <span class="num-dot" style="left:384px;top:26px">4</span>
  <svg class="abs" style="left:211px;top:93px" width="236" height="10" aria-hidden="true"><polygon points="0,0 236,0 228,9 8,9" fill="#c8c8c8"/></svg>

  <div class="about-col" style="left:214px">
    <h4>Global Access, Local Resources</h4><em>Active Value Creation</em>
    <p>Global network provides access to emerging opportunities which are proprietary</p>
    <p>Our local team is experienced in developing best fit operating model and operating structure</p>
    <p>Backed by a reputable group of investors with deep connectivity and relationships in the local markets</p>
  </div>
  <div class="about-col" style="left:336px">
    <h4>Our Partnerships Come First</h4><em>Delivering Growth</em>
    <p>Focused value add investor with aligned objectives with partner brand</p>
    <p>Develop and enhance brand local positioning, retail channels and regional partnerships</p>
    <p>Our subsidiaries are operated by teams with extensive operational expertise in brand management</p>
  </div>

  <div class="brand on-light" style="left:12px;top:243px;font-size:6px"><i></i>Harborlight Equity</div>
  <span class="url">www.harborlight-equity.example</span>
  <span class="page-no">5</span>
</section>

<section class="slide col-r row-3 light">
  <div class="tab"></div>
  <h2 class="abs slide-title" style="top:12px">Global Growth with Local Expertise: Harborlight Solution</h2>

  <p class="issue" style="top:43px"><span class="dot">1</span>International brands are looking to <b>expand</b> into emerging markets to boost gross <b>profit margins and sales volumes</b></p>
  <p class="issue" style="top:72px"><span class="dot">2</span><b>Shelf space is limited</b> in developed markets for emerging brands, <b>due to intense competition and high customer acquisition cost</b></p>
  <p class="issue" style="top:101px"><span class="dot">3</span>Expansion in emerging markets is an <b>intensive capital proposition</b> which can be risky due to lack of local <b>execution skills and market knowledge</b></p>

  <p class="abs phase-title">Illustrative Overview of Retail Growth Phases</p>
  <svg class="abs" style="left:14px;top:150px" width="250" height="70" aria-hidden="true" fill="none" stroke="#555" stroke-width="1.2">
    <circle cx="30" cy="22" r="7"/><path d="M26 30h8M27 33h6M30 8v-4M18 14l-3-3M42 14l3-3"/>
    <g fill="#555" stroke="none"><rect x="82" y="28" width="4" height="8"/><rect x="89" y="22" width="4" height="14"/><rect x="96" y="16" width="4" height="20"/><rect x="103" y="10" width="4" height="26"/></g>
    <path d="M80 26l10-8 6 4 12-10"/>
    <path d="M150 34v-12M150 22c-8 0-10-6-6-10 0-6 10-8 12-2 6 0 6 8 0 10-2 2-4 2-6 2"/>
    <path d="M215 10l10-6 10 6v12l-10 6-10-6zM215 10l10 6 10-6M225 16v12"/>
    <path stroke="#e3262b" stroke-dasharray="2 2" d="M66 2h44v46H66z"/>
  </svg>
  <div class="stage" style="left:19px;top:206px;width:58px"><b>STAGE 1</b>Design and<br>innovation</div>
  <div class="stage" style="left:80px;top:198px;width:60px"><b>STAGE 2</b>Roll-out growth</div>
  <div class="stage" style="left:144px;top:190px;width:58px"><b>STAGE 3</b>Maturity</div>
  <div class="stage" style="left:205px;top:181px;width:56px"><b>STAGE 4</b>Reinvention</div>
  <svg class="abs" style="left:268px;top:43px" width="18" height="200" aria-hidden="true"><polygon points="2,0 14,100 2,200 5,100" fill="#e3262b"/></svg>

  <div class="benefit" style="top:40px;height:94px">
    <h4>Key Benefits for Retail Brand</h4>
    <ul>
      <li>Fully funded expansion into new markets based on agreed business model among retail brand and Harborlight Equity</li>
      <li>Decreased operating risk by partnering with an experienced firm in emerging markets</li>
      <li>Access to tier 1 retail locations</li>
      <li>Expansion of global marketing and public relation campaigns into local markets</li>
    </ul>
  </div>
  <div class="benefit" style="top:142px;height:101px">
    <h4>Key Benefits for Harborlight Equity</h4>
    <ul>
      <li>Access to emerging brands looking at MENA region as an emerging retail market</li>
      <li>Partner with a successful brand with a proven international business model</li>
      <li>Option to scale up through corporate development in new markets, licensing and/or sub-franchising</li>
      <li>Locally adapted marketing and branding to include global content</li>
    </ul>
  </div>

  <div class="brand on-light" style="left:12px;top:243px;font-size:6px"><i></i>Harborlight Equity</div>
  <span class="url">www.harborlight-equity.example</span>
  <span class="page-no">6</span>
</section>

<section class="slide col-l row-4 light">
  <div class="tab"></div>
  <h2 class="abs slide-title" style="top:12px">How Does Harborlight Turn Opportunity into Business Case?</h2>
  <p class="abs subhead" style="left:18px;top:55px">3 key elements are fundamental to Harborlight Equity value creation approach</p>

  <div class="case-row" style="top:73px;height:48px">
    <svg class="case-icon" viewBox="0 0 52 48" aria-hidden="true" fill="none" stroke-width="1.4">
      <circle cx="26" cy="24" r="12" stroke="#e3262b"/><path d="M14 24h24M26 12v24M20 14c-4 6-4 14 0 20M32 14c4 6 4 14 0 20" stroke="#e3262b"/>
      <path d="M8 18a19 19 0 0 1 30-12M44 30a19 19 0 0 1-30 12" stroke="#777"/>
    </svg>
    <div class="case-label" style="background:#0d0d0d">Access to Emerging Markets</div>
    <span class="num-dot" style="left:68px;top:-5px">1</span>
    <ul class="case-text">
      <li>Access to <b>highly attractive retail developing countries</b> such as UAE, Saudi Arabia, Kuwait, Qatar, Nigeria, South Africa among others</li>
      <li><b>Our team is on the ground</b> with deep <b>regional knowledge, significant relationships and operational experience</b> for market entry strategies in emerging markets</li>
    </ul>
  </div>

  <div class="case-row" style="top:127px;height:50px">
    <svg class="case-icon" viewBox="0 0 52 50" aria-hidden="true" fill="none" stroke-width="1.4">
      <path d="M10 22h6v20h-6zM16 24l6-12c2-4 6-2 5 2l-2 6h10c3 0 4 3 2 5l-3 13c-1 3-3 4-6 4H16" stroke="#777"/>
      <rect x="32" y="34" width="12" height="10" stroke="#e3262b"/><path d="M35 34v-4a3 3 0 0 1 6 0v4" stroke="#e3262b"/>
    </svg>
    <div class="case-label" style="background:var(--red)">Local Capital</div>
    <span class="num-dot" style="left:68px;top:-5px">2</span>
    <ul class="case-text">
      <li><b>Harborlight Equity funds market entry, development of business network and omni-channels</b> for the partner brands through the <b>establishment of local companies</b></li>
      <li><b>Backed by a group of professional venture capital investors</b> from the GCC region and supported by <b>international advisors and sector consultants</b></li>
    </ul>
  </div>

  <div class="case-row" style="top:183px;height:51px">
    <svg class="case-icon" viewBox="0 0 52 51" aria-hidden="true" fill="none" stroke-width="1.4">
      <circle cx="18" cy="16" r="7" stroke="#777"/><path d="M4 44c0-10 6-16 14-16s14 6 14 16z" stroke="#777"/>
      <circle cx="34" cy="18" r="6" stroke="#e3262b"/><path d="M34 28c7 0 12 6 12 16" stroke="#e3262b"/>
    </svg>
    <div class="case-label" style="background:var(--grey)">Professional Management</div>
    <span class="num-dot" style="left:68px;top:-5px">3</span>
    <ul class="case-text">
      <li><b>A qualified team of professionals</b> with sector specific expertise across <b>strategy, branding, marketing, online and social media activations, financial management</b></li>
      <li>Aggressive <b>corporate development</b> through various methods, including retail partnerships, licensing, franchise, collaboration depending on target local market</li>
    </ul>
  </div>

  <div class="brand on-light" style="left:12px;top:243px;font-size:6px"><i></i>Harborlight Equity</div>
  <span class="url">www.harborlight-equity.example</span>
  <span class="page-no">7</span>
</section>

<section class="slide col-r row-4 dark">
  <div class="photo photo-skyline" role="img" aria-label="Night photograph of a highway through illuminated city towers"></div>
  <div class="brand on-dark" style="left:338px;top:50px;font-size:10px"><i></i>Harborlight Equity</div>
  <div class="abs" style="left:0;top:150px;width:31px;height:52px;background:var(--red);opacity:.85"></div>
  <div class="abs" style="left:235px;top:151px;width:235px;height:55px;background:var(--red);opacity:.85"></div>
  <div class="divider-vline" style="left:35px;top:148px;height:58px"></div>
  <div class="divider-hline" style="left:35px;width:200px;top:184px"></div>
  <h2 class="abs divider-title" style="left:43px;top:158px">SECTION 2 :</h2>
  <p class="abs divider-sub" style="left:47px;top:189px">OUR INVESTMENTS</p>
</section>

</body>
</html>
```